Beautiful Upgraded Single Story Home in Brindlemere...SOLD in 3 days for top $$!

This is a 6.5" x 11" EDDM postcard. Please use the indicia files and 6.5" x 11" template attached in the brief.
Updates

Project Deadline Extended
Reason: We are still working on the details for one of the postcards. Thanks

Target Market(s)

Listings

Font styles to use
Serif

Colors
33b8a4

Requirements
Must have
• Call me if you are interested in getting the most amount of equity out of your home!
• Marisol Pendry (555) 417-2963 and Tamsin Okavell (555) 730-4186
• Marisol@TeamOkavell.example and Tamsin@TeamOkavell.example
• Harbor Ridge Homes
• The Key to your Real Estate Needs!
• (At bottom of postcard) "If you are currently listed with a licensed Realtor, this is not intended as solicitation"
Nice to have
• The Front Should be the Property Picture and "In Escrow in 3 Days!"

```html
<!DOCTYPE html>
<html lang="en">
<head>
<meta charset="utf-8">
<title>Harbor Ridge Homes – In Escrow Postcard</title>
<link rel="stylesheet" href="https://fonts.googleapis.com/css2?family=Inter:wght@700;800&family=Yellowtail&family=Nunito+Sans:wght@400;600&display=swap">
<style>
  :root {
    --teal: #33b8a4;
    --red: #e8202a;
    --ink: #1c1c1c;
    --white: #ffffff;
    --sky-top: #0a6fc4;
    --sky-mid: #5fa9e2;
    --cloud: #dfe9f2;
    --grass: #6dbb3c;
    --page: #ffffff;
  }
  * { margin: 0; padding: 0; box-sizing: border-box; }
  html, body { width: 1200px; height: 1200px; overflow: hidden; background: var(--page); }
  .canvas { position: relative; width: 1200px; height: 1200px; }

  .card { position: absolute; overflow: hidden; }
  .card-front { left: 65px; top: 130px; width: 521px; height: 938px; }
  .card-back { left: 628px; top: 124px; width: 518px; height: 951px; background: var(--white); box-shadow: 0 0 10px rgba(0,0,0,0.08); }

  .property-photo {
    position: absolute; inset: 0;
    background: linear-gradient(180deg, var(--sky-top) 0%, var(--sky-mid) 35%, var(--cloud) 62%, #d9dcd8 80%, var(--grass) 88%, #58a52c 100%);
  }

  .brand-box {
    position: absolute; left: 173px; top: 106px; width: 176px; height: 82px;
    background: #f2f0ea; border: 3px solid var(--ink);
    display: flex; align-items: center; justify-content: center; text-align: center;
    font-family: "Nunito Sans", sans-serif; font-weight: 600; font-size: 19px; line-height: 1.15; color: var(--ink);
  }

  .headline {
    position: absolute; left: 69px; top: 196px;
    font-family: "Inter", sans-serif; font-weight: 800; font-size: 92px; line-height: 74px;
    letter-spacing: -0.05em; color: var(--white);
  }
  .headline .accent { color: var(--red); }

  .tagline-band {
    position: absolute; left: 0; top: 362px; width: 333px; height: 22px;
    background: var(--red); color: var(--white);
    font-family: "Nunito Sans", sans-serif; font-weight: 600; font-size: 15px; line-height: 22px;
    padding-left: 72px; white-space: nowrap;
  }

  .listing-title {
    position: absolute; left: 0; width: 100%; top: 418px; text-align: center;
    font-family: "Yellowtail", cursive; font-size: 30px; line-height: 34px; color: var(--ink);
  }
  .listing-result {
    position: absolute; left: 0; width: 100%; top: 496px; text-align: center;
    font-family: "Nunito Sans", sans-serif; font-weight: 600; font-size: 16px; color: var(--red);
  }

  .disclaimer {
    position: absolute; left: 0; width: 100%; top: 860px; text-align: center;
    font-family: "Nunito Sans", sans-serif; font-size: 14px; line-height: 21px; color: var(--ink);
  }

  .contact-block { position: absolute; left: 32px; top: 634px; font-family: "Nunito Sans", sans-serif; color: var(--ink); }
  .call-out { font-size: 15.5px; line-height: 20px; width: 280px; }
  .call-out .highlight { color: var(--teal); }
  .agent { margin-top: 22px; }
  .agent + .agent { margin-top: 24px; }
  .agent-name { font-size: 19px; font-weight: 600; line-height: 24px; }
  .agent-phone { font-size: 20px; font-weight: 600; color: var(--teal); line-height: 26px; }
  .agent-email { font-size: 14px; color: var(--teal); line-height: 18px; }
</style>
</head>
<body>
<div class="canvas">
  <section class="card card-front">
    <div class="property-photo" role="img" aria-label="Photo of a two-level stucco and stone home with a dark tile roof, trees and lawn under a blue sky"></div>
    <div class="brand-box">Harbor Ridge<br>Homes</div>
    <h1 class="headline">In Escrow<br>in <span class="accent">3 Days!</span></h1>
    <div class="tagline-band">The Key to your Real Estate Needs!</div>
    <p class="listing-title">Beautiful Upgraded Single<br>Story Home in Brindlemere...</p>
    <p class="listing-result">SOLD in 3 days for top $$!</p>
    <p class="disclaimer">If you are currently listed with a licensed Realtor,<br>this is not intended as solicitation</p>
  </section>

  <section class="card card-back">
    <div class="contact-block">
      <p class="call-out"><span class="highlight">Call me</span> if you are interested in getting the most amount of equity out of your home!</p>
      <div class="agent">
        <p class="agent-name">Marisol Pendry</p>
        <p class="agent-phone">(555) 417-2963</p>
        <p class="agent-email">Marisol@TeamOkavell.example</p>
      </div>
      <div class="agent">
        <p class="agent-name">Tamsin Okavell</p>
        <p class="agent-phone">(555) 730-4186</p>
        <p class="agent-email">Tamsin@TeamOkavell.example</p>
      </div>
    </div>
  </section>
</div>
</body>
</html>
```